Business Card Design

We are looking for a business card designed for our landscaping company. We do landscaping installation & Maintenance Services. We would like to see designs that have basic landscaping in background. We also think it is important to have both of our names and phone numbers on the card. We need something that stands out a little whether it is shape of the card or thickness or design.

Industry/Entity Type

Business

Contact Information for Business Card

Prairie Oak Yardworks, prairieoakyard@mailbox-demo.net, Dale Pruitt 555-613-2907, Marcus Delgado 555-287-4163

```html
<!DOCTYPE html>
<html lang="en">
<head>
<meta charset="utf-8">
<title>Prairie Oak Yardworks – Business Card</title>
<link rel="stylesheet" href="https://fonts.googleapis.com/css2?family=Questrial&display=swap">
<style>
  :root {
    --backdrop: #2b2b2b;
    --card-paper: #f3f4ef;
    --scene-light: #eef0ea;
    --scene-mid: #e2e6dc;
    --leaf-green: #6cb84a;
    --leaf-green-dark: #3e9a3a;
    --wave-light: #9fd07f;
    --soil-brown: #b08f5c;
    --bark-brown: #6d5038;
    --ink-grey: #4a4a4a;
  }
  * { margin: 0; padding: 0; box-sizing: border-box; }
  html, body {
    width: 1200px; height: 720px; overflow: hidden;
    background: var(--backdrop);
  }
  .canvas {
    position: relative; width: 1200px; height: 720px;
    display: flex; align-items: center; justify-content: center;
  }
  .business-card {
    position: relative; width: 1000px; height: 580px;
    border-radius: 80px; overflow: hidden;
    background: var(--card-paper);
    font-family: "Questrial", sans-serif;
  }
  .card-art { position: absolute; inset: 0; width: 100%; height: 100%; }
  .company-name {
    position: absolute; top: 92px; left: 380px; width: 560px;
    text-align: center;
    font-size: 52px; line-height: 1.1; letter-spacing: 0.5px;
    color: var(--leaf-green-dark);
  }
  .contact-block {
    position: absolute; left: 92px; top: 310px;
    color: var(--leaf-green-dark);
  }
  .contact-person { margin-bottom: 18px; }
  .person-name { font-size: 34px; line-height: 1.1; }
  .person-phone {
    display: flex; align-items: center; gap: 10px;
    font-size: 24px; color: var(--ink-grey); margin-top: 2px;
  }
  .phone-icon { width: 20px; height: 20px; fill: var(--ink-grey); }
  .contact-email { font-size: 26px; margin-top: 6px; }
</style>
</head>
<body>
<main class="canvas">
  <article class="business-card">
    <svg class="card-art" viewBox="0 0 1000 580" preserveAspectRatio="none">
      <defs>
        <linearGradient id="sceneTone" x1="0" y1="0" x2="0" y2="1">
          <stop offset="0" stop-color="var(--scene-mid)"/>
          <stop offset="0.45" stop-color="var(--scene-light)"/>
          <stop offset="1" stop-color="#f1f2ed"/>
        </linearGradient>
      </defs>
      <rect class="background-scene" width="1000" height="580" fill="url(#sceneTone)"
            role="img" aria-label="Faded photo of a landscaped front yard with lawn, flower beds and a white porch"/>
      <path class="wave-brown" d="M0 520 C 300 600, 640 420, 1000 230 L1000 580 L0 580 Z" fill="var(--bark-brown)"/>
      <path class="wave-tan" d="M0 540 C 320 610, 650 440, 1000 250 L1000 580 L0 580 Z" fill="var(--soil-brown)"/>
      <path class="wave-line" d="M0 556 C 330 622, 660 458, 1000 268 L1000 580 L0 580 Z" fill="#ffffff"/>
      <path class="wave-green" d="M0 562 C 330 628, 665 464, 1000 274 L1000 580 L0 580 Z" fill="var(--leaf-green)"/>
      <path class="wave-highlight" d="M420 580 C 640 520, 820 420, 1000 300 L1000 330 C 820 450, 660 540, 480 580 Z" fill="var(--wave-light)" opacity="0.45"/>
    </svg>

    <h1 class="company-name">Prairie Oak Yardworks</h1>

    <section class="contact-block">
      <div class="contact-person">
        <p class="person-name">Dale Pruitt</p>
        <p class="person-phone">
          <svg class="phone-icon" viewBox="0 0 24 24" aria-hidden="true"><path d="M6.6 10.8a15.1 15.1 0 0 0 6.6 6.6l2.2-2.2a1 1 0 0 1 1-.25 11.4 11.4 0 0 0 3.6.57 1 1 0 0 1 1 1V20a1 1 0 0 1-1 1A17 17 0 0 1 3 4a1 1 0 0 1 1-1h3.5a1 1 0 0 1 1 1c0 1.25.2 2.45.57 3.57a1 1 0 0 1-.25 1z"/></svg>
          555-613-2907
        </p>
      </div>
      <div class="contact-person">
        <p class="person-name">Marcus Delgado</p>
        <p class="person-phone">
          <svg class="phone-icon" viewBox="0 0 24 24" aria-hidden="true"><path d="M6.6 10.8a15.1 15.1 0 0 0 6.6 6.6l2.2-2.2a1 1 0 0 1 1-.25 11.4 11.4 0 0 0 3.6.57 1 1 0 0 1 1 1V20a1 1 0 0 1-1 1A17 17 0 0 1 3 4a1 1 0 0 1 1-1h3.5a1 1 0 0 1 1 1c0 1.25.2 2.45.57 3.57a1 1 0 0 1-.25 1z"/></svg>
          555-287-4163
        </p>
      </div>
      <p class="contact-email">prairieoakyard@mailbox-demo.net</p>
    </section>
  </article>
</main>
</body>
</html>
```